Ridgeline Fluidworks needs a website describing the repair business we are in.

Ridgeline Fluidworks is a full hydraulic repair facility. We have 2 shops. We repair and service all hydraulic cylinders, pneumatic cylinders, hydraulic pumps, motors, valves and gearboxes. Our services range from large industrial plants to the individual that owns one piece of equipment. We also offer removal and install of cylinders. Along with free pick up and delivery, within a certain distance which is usually 100 miles from one of our shops.

With over 30 years experience in the hydraulic business, we can repair or replace any job. There is not a job too big or too small, we service them all.

We have customers that send whole pieces of equipment to us to do complete overhauls on all the hydraulics. Ranging from a country club green roller to a 10 ton boom truck.

Target Market(s)

Industrial plants, road builders, dirt work companies, general contractors, owners of industrial equipment (bulldozers, excavators, loaders, scrapers, motor graders, etc.

Industry/Entity Type

Hydraulic

Number of Pages Required

5+ page

Font styles to use
Sans Serif

Colors
ec1f27
ffffff
aaaaaa

Requirements
Must have
• Information about what we offer and pictures of jobs completed.
Nice to have
• Nice stock photos of jobsites and industrial plants.
Should not have
• Any sort of comical characters.

```html
<!DOCTYPE html>
<html lang="en">
<head>
<meta charset="utf-8">
<title>Ridgeline Fluidworks – Hydraulic Repair</title>
<link href="https://fonts.googleapis.com/css2?family=Poppins:wght@300;400;500;600&display=swap" rel="stylesheet">
<style>
:root{
  --red:#ec1f27;
  --white:#ffffff;
  --grey:#aaaaaa;
  --ink:#222428;
  --text:#55585e;
  --muted:#8a8d93;
  --panel:#f4f5f9;
  --card:#f3f3f3;
  --footer:#3b3f47;
}
*{margin:0;padding:0;box-sizing:border-box}
html,body{width:1200px;height:2995px;overflow:hidden}
body{position:relative;background:var(--white);font-family:"Poppins",Arial,sans-serif;color:var(--text)}
.abs{position:absolute}
.photo{position:absolute;display:block}

/* header */
.site-header{position:absolute;left:0;top:0;width:1200px;height:104px;background:var(--white)}
.brand{position:absolute;left:156px;top:24px;display:flex;align-items:center;gap:10px}
.brand-mark{width:46px;height:46px;border-radius:50%;background:var(--red)}
.brand-name{font-size:16px;font-weight:600;color:var(--red);letter-spacing:.3px}
.call{position:absolute;left:556px;top:18px;font-size:14px;color:var(--ink);display:flex;align-items:center;gap:6px}
.call b{color:var(--red);font-weight:500}
.social{position:absolute;display:flex;gap:6px}
.social span{width:22px;height:22px;border-radius:50%;background:var(--grey)}
.social span.on{background:var(--red)}
.btn{position:absolute;display:flex;align-items:center;justify-content:center;border-radius:20px;font-size:10px;font-weight:500;letter-spacing:1.4px;text-transform:uppercase}
.btn-outline-red{border:1.5px solid var(--red);color:var(--red);background:var(--white)}
.btn-outline-white{border:1.5px solid var(--white);color:var(--white)}
.btn-red{background:var(--red);color:var(--white)}
.nav{position:absolute;left:424px;top:66px;display:flex;gap:0;font-size:10.5px;letter-spacing:1.2px;color:var(--ink);text-transform:uppercase}
.nav a{display:block;padding:0 18px;text-decoration:none;color:inherit}
.nav a:first-child{padding-left:0}
.nav a.active{color:var(--red)}
.nav-bar{position:absolute;left:416px;top:100px;width:48px;height:3px;background:var(--red)}

/* hero */
.hero-photo{left:0;top:104px;width:1200px;height:400px;background:linear-gradient(120deg,#6d7278 0%,#9ca1a5 35%,#5d6166 60%,#868b90 100%)}
.hero-title{left:156px;top:208px;font-size:28px;line-height:36px;color:var(--white);font-weight:400}
.hero-text{left:156px;top:296px;width:520px;font-size:12.5px;line-height:20px;color:var(--white)}
.circle-arrow{position:absolute;width:32px;height:32px;border-radius:50%;display:flex;align-items:center;justify-content:center}
.circle-arrow.outline{border:1.5px solid var(--white)}
.circle-arrow.solid{background:var(--white)}
.circle-arrow.grey{border:1.5px solid #c9c9c9;background:var(--white);width:28px;height:28px}
.circle-arrow.dark{background:#6a6d72;width:28px;height:28px}

/* offer */
.offer-band{left:0;top:504px;width:1200px;height:240px;background:linear-gradient(100deg,#d8232a,#e5242b 50%,#cf1f26)}
.section-title{position:absolute;left:0;width:1200px;text-align:center;font-size:28px;font-weight:400;color:var(--ink);display:flex;justify-content:center;align-items:center;gap:28px}
.section-title em{font-style:normal;color:var(--red)}
.section-title i{display:block;width:56px;height:1px;background:#cfd0d4}
.section-title.light{color:var(--white)}
.section-title.light i{background:rgba(255,255,255,.6)}
.card{position:absolute;width:280px;background:var(--card);box-shadow:0 2px 4px rgba(0,0,0,.08)}
.card .photo{position:relative;width:100%}
.card-body{text-align:center}
.card-title{font-size:17px;color:var(--ink);font-weight:400}
.dash{width:40px;height:0;border-top:1.5px dashed var(--grey);margin:8px auto 0}
.read-more{font-size:9.5px;letter-spacing:1.4px;color:#5a5d63;text-transform:uppercase}
.read-more.hot{color:var(--red)}

/* about */
.about-photo{left:230px;top:920px;width:360px;height:360px;border-radius:50%;background:radial-gradient(circle at 40% 40%,#f3c024,#c99a1a 45%,#4c4a44 100%)}
.about-title{left:612px;top:938px;font-size:28px;color:var(--ink)}
.about-title em{font-style:normal;color:var(--red)}
.about-lead{left:612px;top:996px;width:360px;font-size:12.5px;line-height:19px;color:var(--ink)}
.about-text{position:absolute;left:612px;width:360px;font-size:11.5px;line-height:17px;color:var(--muted)}

/* jobs */
.jobs{left:0;top:1344px;width:1200px;height:766px;background:var(--panel)}
.job-tile{position:absolute}
.job-feature{background:var(--red);color:var(--white);display:flex;align-items:center;justify-content:center;flex-direction:column;font-size:15px;font-weight:500}

/* blog */
.date-pill{position:absolute;left:50%;transform:translateX(-50%);top:-14px;background:var(--red);color:var(--white);font-size:10px;padding:4px 16px;border-radius:14px;white-space:nowrap}
.blog-body{position:relative;text-align:center}

/* footer */
.footer-left{left:0;top:2650px;width:484px;height:345px;background:var(--footer)}
.footer-right{left:484px;top:2650px;width:716px;height:345px;background:linear-gradient(180deg,#2e3138,#474a51 55%,#2a2c31)}
.f-head{position:absolute;font-size:15px;color:var(--white)}
.f-line{position:absolute;font-size:11px;color:#b9bcc2}
.field{position:absolute;left:536px;width:380px;border-bottom:1px solid rgba(255,255,255,.25);font-size:10.5px;color:var(--white);padding-bottom:8px}
</style>
</head>
<body>

<header class="site-header">
  <div class="brand"><span class="brand-mark"></span><span class="brand-name">Ridgeline Fluidworks</span></div>
  <div class="call"><b>Call Us:</b>
    <svg width="16" height="16" viewBox="0 0 24 24"><circle cx="12" cy="12" r="11" fill="none" stroke="#ec1f27" stroke-width="2"/><path d="M8.5 6.5l2 2-1.2 1.5a8 8 0 0 0 4.7 4.7l1.5-1.2 2 2-1.5 1.8c-4.5-.5-8.5-4.5-9-9z" fill="#ec1f27"/></svg>
    555 - 014 - 2280</div>
  <div class="social" style="left:776px;top:14px"><span></span><span class="on"></span><span></span></div>
  <div class="btn btn-outline-red" style="left:892px;top:12px;width:152px;height:34px">Request a Quote</div>
  <nav class="nav">
    <a class="active">Home</a><a>About Us</a><a>Services</a><a>Partner</a><a>Gallery</a><a>Blog</a><a>Contact</a>
  </nav>
  <div class="nav-bar"></div>
</header>

<section>
  <div class="photo hero-photo" role="img" aria-label="Industrial plant with large steel pipework and valves"></div>
  <h1 class="abs hero-title">Our Services<br>Range From Large Industrial</h1>
  <p class="abs hero-text">We also offer removal and install of cylinders Along with free pick-up and delivery.</p>
  <div class="btn btn-outline-white" style="left:156px;top:360px;width:144px;height:32px">Explore More</div>
  <div class="circle-arrow outline" style="left:1012px;top:266px"><svg width="12" height="10" viewBox="0 0 12 10"><path d="M11 5H1M5 1L1 5l4 4" stroke="#fff" stroke-width="1.5" fill="none"/></svg></div>
  <div class="circle-arrow solid" style="left:1012px;top:308px"><svg width="12" height="10" viewBox="0 0 12 10"><path d="M1 5h10M7 1l4 4-4 4" stroke="#222" stroke-width="1.5" fill="none"/></svg></div>
</section>

<section>
  <div class="photo offer-band" role="img" aria-label="Industrial plant pipework under a red tint"></div>
  <h2 class="section-title light" style="top:540px"><i></i>What We Offer<i></i></h2>

  <article class="card" style="left:156px;top:616px">
    <div class="photo" style="height:128px;background:linear-gradient(135deg,#2f6fb0,#e07a22 55%,#8a8f95)" role="img" aria-label="Hydraulic cylinder on an orange machine"></div>
    <div class="card-body" style="height:112px;padding-top:24px"><div class="card-title">Hydraulic Cylinders</div><div class="dash"></div><div class="read-more" style="margin-top:22px">Read More &rarr;</div></div>
  </article>
  <article class="card" style="left:460px;top:616px;background:var(--white);box-shadow:0 4px 10px rgba(0,0,0,.12)">
    <div class="photo" style="height:128px;background:linear-gradient(135deg,#2b2d31,#8d9297 50%,#d3d5d8)" role="img" aria-label="Row of pneumatic cylinders in an assembly line"></div>
    <div class="card-body" style="height:112px;padding-top:24px"><div class="card-title">Pneumatic Cylinders</div><div class="dash"></div><div class="read-more hot" style="margin-top:22px">Read More &rarr;</div></div>
  </article>
  <article class="card" style="left:764px;top:616px">
    <div class="photo" style="height:128px;background:linear-gradient(135deg,#9aa0a6,#2a4fa8 50%,#6b7076)" role="img" aria-label="Blue hydraulic pumps in a pump station"></div>
    <div class="card-body" style="height:112px;padding-top:24px"><div class="card-title">Hydraulic Pumps</div><div class="dash"></div><div class="read-more" style="margin-top:22px">Read More &rarr;</div></div>
  </article>

  <div class="circle-arrow grey" style="left:102px;top:728px"><svg width="10" height="8" viewBox="0 0 12 10"><path d="M11 5H1M5 1L1 5l4 4" stroke="#666" stroke-width="1.5" fill="none"/></svg></div>
  <div class="circle-arrow dark" style="left:1070px;top:728px"><svg width="10" height="8" viewBox="0 0 12 10"><path d="M1 5h10M7 1l4 4-4 4" stroke="#fff" stroke-width="1.5" fill="none"/></svg></div>
</section>

<section>
  <div class="photo about-photo" role="img" aria-label="Close-up of a yellow hydraulic cylinder with hose fittings"></div>
  <h2 class="abs about-title">About <em>Us</em></h2>
  <p class="abs about-lead">We repair and service all hydraulic cylinders, pneumatic cylinders, hydraulic pumps, motors, valves and gearboxes.</p>
  <p class="about-text" style="top:1066px">Our services range from large industrial plants to the individual that owns one piece of equipment. We also offer removal and install of cylinders.</p>
  <p class="about-text" style="top:1136px">With over 30 years' experience in the hydraulic business, we can repair or replace any job. There is not a job too big or too small, we service them all.</p>
  <div class="btn btn-outline-red" style="left:612px;top:1216px;width:144px;height:32px">Discover More</div>
</section>

<section>
  <div class="abs jobs"></div>
  <h2 class="section-title" style="top:1398px"><i></i><span>Completed <em>Jobs</em></span><i></i></h2>
  <div class="photo job-tile" style="left:80px;top:1460px;width:320px;height:320px;background:linear-gradient(160deg,#3a3a3a,#9c9ea1 45%,#c8c9cb 70%,#8a7b60)" role="img" aria-label="Refurbished hydraulic cylinders on a pallet next to an oil drum"></div>
  <div class="job-tile job-feature" style="left:432px;top:1460px;width:336px;height:168px">Hydraulic Pumps Service
    <svg width="22" height="22" viewBox="0 0 24 24" style="margin-top:10px"><path d="M10 14a4 4 0 0 0 5.7 0l3-3a4 4 0 0 0-5.7-5.7l-1 1M14 10a4 4 0 0 0-5.7 0l-3 3a4 4 0 0 0 5.7 5.7l1-1" stroke="#fff" stroke-width="2" fill="none"/></svg></div>
  <div class="photo job-tile" style="left:800px;top:1460px;width:320px;height:320px;background:linear-gradient(160deg,#1f2023,#5a5c60 45%,#b58a52 70%,#2b55a0)" role="img" aria-label="Blue hydraulic pump strapped to a wooden pallet"></div>
  <div class="photo job-tile" style="left:80px;top:1814px;width:320px;height:166px;background:linear-gradient(150deg,#6f6a60,#b49a5a 50%,#4d4b47)" role="img" aria-label="Yellow cylinders laid across a pallet"></div>
  <div class="photo job-tile" style="left:432px;top:1660px;width:336px;height:320px;background:linear-gradient(170deg,#7a4a3a,#8e8f92 35%,#3b3c3f 65%,#c9a33a)" role="img" aria-label="Long yellow hydraulic cylinder on a flatbed trailer"></div>
  <div class="photo job-tile" style="left:800px;top:1814px;width:320px;height:166px;background:linear-gradient(150deg,#c9c9c9,#d8553a 45%,#b63b2a 70%,#8a8a8a)" role="img" aria-label="Red telescopic cylinder on a workshop floor"></div>
  <div class="btn btn-outline-red" style="left:544px;top:2012px;width:112px;height:32px">View All</div>
</section>

<section>
  <h2 class="section-title" style="top:2166px"><i></i><span>Latest <em>Blog</em></span><i></i></h2>

  <article class="card" style="left:156px;top:2232px">
    <div class="photo" style="height:158px;background:linear-gradient(135deg,#c6cbd0,#2f8a5a 45%,#7f868c)" role="img" aria-label="Green pumps in an industrial plant"></div>
    <div class="blog-body" style="height:132px;padding-top:36px"><span class="date-pill">12 SEP, 2017</span><div style="font-size:13px;line-height:18px;color:var(--ink)">There are many variations of<br>passages</div><div class="read-more" style="margin-top:22px">Read More &rarr;</div></div>
  </article>
  <article class="card" style="left:460px;top:2232px;background:var(--white);box-shadow:0 4px 10px rgba(0,0,0,.12)">
    <div class="photo" style="height:158px;background:linear-gradient(135deg,#1e1e1e,#c42a2a 45%,#8a6a4a)" role="img" aria-label="Red hydraulic boom arm on a jobsite"></div>
    <div class="blog-body" style="height:132px;padding-top:36px"><span class="date-pill">20 SEP, 2017</span><div style="font-size:13px;line-height:18px;color:var(--ink)">There are many variations of<br>passages</div><div class="read-more" style="margin-top:22px">Read More &rarr;</div></div>
  </article>
  <article class="card" style="left:764px;top:2232px">
    <div class="photo" style="height:158px;background:linear-gradient(135deg,#b7c0c8,#2a4fa8 50%,#8e959b)" role="img" aria-label="Blue pump units in a plant room"></div>
    <div class="blog-body" style="height:132px;padding-top:36px"><span class="date-pill">30 SEP, 2017</span><div style="font-size:13px;line-height:18px;color:var(--ink)">There are many variations<br>of passages</div><div class="read-more" style="margin-top:22px">Read More &rarr;</div></div>
  </article>

  <div class="circle-arrow grey" style="left:104px;top:2376px"><svg width="10" height="8" viewBox="0 0 12 10"><path d="M11 5H1M5 1L1 5l4 4" stroke="#666" stroke-width="1.5" fill="none"/></svg></div>
  <div class="circle-arrow grey" style="left:1068px;top:2376px"><svg width="10" height="8" viewBox="0 0 12 10"><path d="M1 5h10M7 1l4 4-4 4" stroke="#666" stroke-width="1.5" fill="none"/></svg></div>
  <div class="btn btn-outline-red" style="left:544px;top:2552px;width:112px;height:32px">View All</div>
</section>

<footer>
  <div class="abs footer-left"></div>
  <div class="photo footer-right" role="img" aria-label="Industrial plant at dusk with dark pipework"></div>

  <div class="f-head" style="left:156px;top:2712px">Contact us</div>
  <div class="abs" style="left:156px;top:2752px;font-size:18px;color:#c9ccd1;font-weight:300">Call Us: 555 - 014 - 2280</div>
  <div class="f-line" style="left:156px;top:2778px">info@ridgelinefluidworks.com</div>
  <div class="f-line" style="left:158px;top:2824px;color:var(--white)">Get Social</div>
  <div class="social" style="left:232px;top:2818px"><span></span><span class="on"></span><span></span></div>
  <div class="abs" style="left:156px;top:2876px;width:328px;height:1px;background:rgba(255,255,255,.12)"></div>
  <div class="f-line" style="left:156px;top:2910px;line-height:17px">© 2018 - <span style="color:var(--red)">Ridgeline Fluidworks</span><br>All Rights Reserved</div>

  <div class="f-head" style="left:536px;top:2714px">Request a Quote</div>
  <div class="field" style="top:2756px">Name</div>
  <div class="field" style="top:2804px">Phone</div>
  <div class="field" style="top:2852px">Email</div>
  <div class="btn btn-red" style="left:536px;top:2900px;width:80px;height:30px">Send</div>
  <svg class="abs" style="left:1006px;top:2712px" width="36" height="36" viewBox="0 0 36 36"><path d="M3 10V3h30v7M3 26v7h30v-7" stroke="#ec1f27" stroke-width="1.5" fill="none"/><path d="M18 28V10M11 17l7-7 7 7" stroke="#ec1f27" stroke-width="1.8" fill="none"/></svg>
</footer>

</body>
</html>
```